IT consultancy business needs logo and business card designed

I need designed business card. it needs to have some wow effect, but simple, corporate and business focused. We provide corporate grade IT services to medium size businesses. These services are IT support over phone, email, in person, VOIP services, IT security , networking - everything that helps business be productivy.

Out tag line will be something along these lines" promoting business growth through use of technology:.

I need a logo designed as well. I am happy to use any colors/theme, perhaps neutral colours, earthy?

Priority: NICE looking, wow design, nice fonts, colors etc... nice logo, business focused but HAS to be modern, wow effect. I will accept anything that looks really cool.

Target Market(s)

Target market are businesses with 20-100 employees. Audience are business decision makers, like general managers, CEO, directors, those are the one seeing this business card;

Industry/Entity Type

Business

Contact Information for Business Card

I am totally flexible, suprise me me something creative:

Dorian Velmek logo on this side(you will design)
managing director ------------------------------- this is line
slogan: technology.delivered.simple

Level 3, 48 Pemberwick Street, Sydney, NSW 2000
dorian@tovrani.com.au
www.tovrani.com.au

back page: logo and slogan: promoting business growth through use of technolog

Requirements
Must have
• Must look modern, cool., wow effect, yet simple and professional.

```html
<!DOCTYPE html>
<html lang="en">
<head>
<meta charset="utf-8">
<title>Tovrani – Business Card</title>
<link rel="stylesheet" href="https://fonts.googleapis.com/css2?family=Exo+2:wght@400;500;600&display=swap">
<style>
  :root {
    --backdrop: #ececed;
    --card: #ffffff;
    --brand-blue: #2f6fb3;
    --name-blue: #4b4fa6;
    --ink: #3a3d46;
    --band-dark: #2a3f7a;
    --band-light: #5fa8dc;
  }
  * { box-sizing: border-box; margin: 0; padding: 0; }
  html, body {
    width: 1200px; height: 735px; overflow: hidden;
    background: var(--backdrop);
    font-family: "Exo 2", Arial, sans-serif;
  }
  .card {
    position: absolute; left: 240px; top: 162px;
    width: 720px; height: 411px;
    background: var(--card);
    box-shadow: 0 2px 10px rgba(0,0,0,0.12);
    overflow: hidden;
  }
  .card-band {
    position: absolute; left: 0; bottom: 0;
    width: 720px; height: 411px;
    background: linear-gradient(90deg, var(--band-dark), var(--band-light));
    clip-path: polygon(0 50%, 100% 86%, 100% 95%, 0 66%);
  }
  .brand {
    position: absolute; left: 44px; top: 48px;
    display: flex; align-items: center; gap: 14px;
  }
  .brand-dot {
    width: 48px; height: 48px; border-radius: 50%;
    background: var(--brand-blue);
  }
  .brand-name {
    font-size: 44px; font-weight: 600; letter-spacing: 3px;
    color: var(--brand-blue); line-height: 1;
  }
  .person { position: absolute; left: 40px; top: 140px; }
  .person-name {
    font-size: 22px; font-weight: 500; letter-spacing: 2px;
    color: var(--name-blue); text-transform: uppercase;
  }
  .person-title { font-size: 14px; color: var(--ink); margin-top: 4px; }
  .address {
    position: absolute; right: 40px; top: 120px;
    text-align: right; font-size: 14px; font-style: normal; font-weight: 500;
    line-height: 1.5; color: var(--ink); width: 260px;
  }
  .contacts {
    position: absolute; right: 40px; top: 200px;
    list-style: none; text-align: right;
    font-size: 13px; color: var(--ink);
  }
  .contacts li {
    display: flex; justify-content: flex-end; align-items: center;
    gap: 8px; height: 22px;
  }
  .contacts svg { width: 13px; height: 13px; fill: var(--brand-blue); }
</style>
</head>
<body>
  <article class="card">
    <div class="card-band" role="img" aria-label="Blue gradient band sweeping across the lower card"></div>

    <header class="brand">
      <span class="brand-dot"></span>
      <span class="brand-name">TOVRANI</span>
    </header>

    <div class="person">
      <p class="person-name">Dorian Velmek</p>
      <p class="person-title">Managing Director</p>
    </div>

    <address class="address">Level 3, 48 Pemberwick Street,<br>Sydney, NSW 2000</address>

    <ul class="contacts">
      <li>012 555 0147
        <svg viewBox="0 0 16 16"><path d="M3 1l3 3-2 2c1 2 3 4 5 5l2-2 3 3-2 3C7 15 1 9 1 3z"/></svg></li>
      <li>012 555 0148
        <svg viewBox="0 0 16 16"><path d="M4 0h8v16H4zM6 2v10h4V2z"/></svg></li>
      <li>012 555 0149
        <svg viewBox="0 0 16 16"><path d="M2 5h12v9H2zM4 1h8v3H4z"/></svg></li>
      <li>dorian@tovrani.com.au
        <svg viewBox="0 0 16 16"><path d="M1 3h14v10H1zM2 4l6 5 6-5z"/></svg></li>
      <li>www.tovrani.com.au
        <svg viewBox="0 0 16 16"><circle cx="8" cy="8" r="7"/></svg></li>
    </ul>
  </article>
</body>
</html>
```